Vellora Solutions Website Creation

Create a business website for custom flexible packaging and MDF products. The www.Kestivo.example website is generic page that you can use to create a similar home page for my business.
Specifically: https://www.kestivo.example/packaging/
https://www.kestivo.example/product/mdf-panels/
Domain is Vel-Lora.example
I would like the page to have a more packaging related look than the MDF/wood.

```html
<!DOCTYPE html>
<html lang="en">
<head>
<meta charset="utf-8">
<title>Vellora Solutions</title>
<link href="https://fonts.googleapis.com/css2?family=Archivo:wght@700;800;900&family=Inter:wght@400;500;600&display=swap" rel="stylesheet">
<style>
:root{
  --blue:#0ea5f5;
  --navy:#1d2645;
  --ink:#111827;
  --text:#2b2f38;
  --pale:#e4f3fd;
  --white:#ffffff;
}
*{box-sizing:border-box;margin:0;padding:0}
html,body{width:1200px;height:2672px;overflow:hidden}
body{position:relative;background:var(--white);font-family:'Inter',sans-serif;color:var(--text)}
.abs{position:absolute}

/* header */
.brand{left:150px;top:52px;display:flex;align-items:center;gap:12px}
.brand-dot{width:46px;height:46px;border-radius:50%;background:var(--blue)}
.brand-name{font-weight:600;font-size:30px;color:var(--navy);letter-spacing:-.3px}
.contact-item{display:flex;gap:14px;align-items:flex-start;top:34px}
.contact-item svg{margin-top:4px}
.contact-label{font-size:13px;font-weight:600;color:var(--ink);letter-spacing:.3px}
.contact-value{font-size:15px;color:var(--ink);margin-top:3px;white-space:nowrap}
.contact-phone{font-family:'Archivo',sans-serif;font-weight:700;font-size:22px;color:var(--blue);margin-top:1px}
.nav{top:99px;left:557px;display:flex;font-size:14px;color:var(--ink)}
.nav a{color:inherit;text-decoration:none;display:block}
.nav .active{color:var(--blue);font-weight:600;border-bottom:2px solid var(--blue);padding-bottom:6px}

/* hero */
.hero{left:0;top:150px;width:1200px;height:488px;background:linear-gradient(100deg,#0a6fb6 0%,#0b86c9 45%,#14a6d6 75%,#0c7fbf 100%)}
.hero-ship{left:505px;top:30px;width:520px;height:370px;border-radius:6px;background:linear-gradient(150deg,rgba(250,120,150,.55),rgba(60,40,70,.5));transform:skewX(-20deg)}
.hero-title{left:150px;top:52px;font-family:'Archivo',sans-serif;font-weight:900;font-size:52px;line-height:63px;color:var(--white)}
.btn{display:inline-block;background:var(--blue);color:var(--white);font-family:'Archivo',sans-serif;font-weight:800;border-radius:30px;text-decoration:none;text-align:center}
.hero-btn{left:150px;top:332px;width:177px;height:58px;line-height:58px;font-size:18px;border-radius:22px}

/* intro */
.intro-title{left:0;top:700px;width:1200px;text-align:center;font-family:'Archivo',sans-serif;font-weight:900;font-size:30px;color:var(--ink)}
.intro-title span{color:var(--blue)}
.rule{height:3px;background:var(--navy)}
.intro-rule{left:571px;top:774px;width:58px}
.intro-text{left:240px;top:822px;width:720px;text-align:center;font-size:14.5px;line-height:22.5px;color:var(--text)}

.card{top:939px;width:441px;height:331px;border-radius:16px;overflow:hidden}
.card-pack{left:150px;background:linear-gradient(180deg,#8cc7e8 0%,#dbe9ef 45%,#6a9b3e 60%,#3e6a22 100%)}
.card-wood{left:607px;background:linear-gradient(160deg,#f6f3ec 0%,#ece6da 55%,#d8d0be 100%)}
.card-body{position:absolute;left:0;top:36px;width:100%;text-align:center}
.card-title{font-family:'Archivo',sans-serif;font-weight:800;font-size:23px;color:var(--navy)}
.card-text{font-size:15px;color:var(--ink);margin-top:10px}
.card-btn{margin-top:18px;width:108px;height:36px;line-height:36px;font-size:12.5px}
.card-badge{left:563px;top:1067px;width:72px;height:72px;border-radius:50%;background:var(--white);box-shadow:0 2px 6px rgba(0,0,0,.15)}
.card-badge i{position:absolute;left:18px;top:18px;width:36px;height:36px;border-radius:50%;background:var(--blue)}
.soft-band{left:0;top:1250px;width:1200px;height:93px;background:linear-gradient(180deg,#ffffff 0%,#e6f3fc 100%)}

/* welcome */
.welcome{left:0;top:1343px;width:1200px;height:547px;background:var(--navy);overflow:hidden}
.welcome-photo{left:180px;top:86px;width:390px;height:390px;border-radius:50%;background:radial-gradient(circle at 45% 45%,#f2efe9 0%,#e0b48a 45%,#9aa57a 80%,#7a7d66 100%)}
.welcome-kicker{left:664px;top:50px;font-family:'Archivo',sans-serif;font-weight:800;font-size:23px;color:var(--white)}
.welcome-title{left:664px;top:84px;font-family:'Archivo',sans-serif;font-weight:900;font-size:54px;line-height:55px;color:var(--white)}
.welcome-title span{color:var(--blue)}
.welcome-rule{left:664px;top:222px;width:58px;background:var(--white)}
.welcome-text{left:664px;top:267px;width:392px;font-size:14px;line-height:19.7px;letter-spacing:-.1px;color:#d4d9e6}
.welcome-btn{left:664px;top:452px;width:115px;height:38px;line-height:38px;font-size:13.5px}

/* features */
.feature{top:1890px;width:400px;height:417px;overflow:hidden}
.feat-forest{left:0;background:linear-gradient(180deg,#4d7a3a 0%,#2f4d22 55%,#5a4a2c 100%)}
.feat-port{left:398px;background:linear-gradient(180deg,#f0c59a 0%,#8fb2c6 35%,#3f5a6c 70%,#4a5560 100%)}
.feat-city{left:800px;background:linear-gradient(210deg,#5aa6e6 0%,#8fc6f0 40%,#f7c97a 70%,#3a78b8 100%)}
.feat-box{position:absolute;left:24px;top:235px;width:345px;height:158px;border-radius:12px;background:rgba(40,40,40,.55);padding:22px 22px}
.feat-title{font-family:'Archivo',sans-serif;font-weight:800;font-size:17px;color:var(--white)}
.feat-text{font-size:12px;line-height:16px;color:#eef0f3;margin-top:8px}
.feat-btn{margin-top:12px;width:86px;height:26px;line-height:26px;font-size:10px}

/* footer */
.footer{left:0;top:2307px;width:1200px;height:365px;background:var(--pale)}
.footer-mark{left:150px;top:118px;font-weight:600;font-size:40px;line-height:48px;color:var(--navy)}
.col-title{font-family:'Archivo',sans-serif;font-weight:800;font-size:15px;color:var(--navy)}
.col-contact{left:490px;top:59px}
.col-menu{left:745px;top:59px}
.col-follow{left:880px;top:59px}
.info-row{display:flex;gap:16px;font-size:12.5px;line-height:18px;color:var(--ink);margin-top:16px}
.info-row svg{flex:none;margin-top:2px}
.menu-list{list-style:none;margin-top:12px;font-size:12.5px;line-height:18px;color:var(--ink)}
.social{display:flex;gap:5px;margin-top:16px}
.social i{width:25px;height:25px;border-radius:50%;background:var(--navy)}
.footer-brand{left:872px;top:167px;display:flex;align-items:center;gap:8px}
.footer-brand i{width:36px;height:36px;border-radius:50%;background:var(--blue)}
.footer-brand span{font-weight:600;font-size:21px;color:var(--navy)}
.footer-rule{left:490px;top:256px;width:558px;height:1px;background:#b9c8d4}
.copyright{left:700px;top:298px;width:345px;text-align:right;font-size:12.5px;color:var(--ink)}
</style>
</head>
<body>

<header>
  <div class="abs brand"><span class="brand-dot"></span><span class="brand-name">Vellora Solutions</span></div>
  <div class="abs contact-item" style="left:555px">
    <svg width="30" height="30" viewBox="0 0 30 30" fill="none" stroke="#0ea5f5" stroke-width="2"><path d="M4 12 L15 4 L26 12 V26 H4 Z"/><path d="M4 12 L15 19 L26 12"/></svg>
    <div><div class="contact-label">EMAIL US</div><div class="contact-value">Ivo.Lund@Vel-Lora.example</div></div>
  </div>
  <div class="abs contact-item" style="left:845px">
    <svg width="34" height="34" viewBox="0 0 34 34" fill="none" stroke="#0ea5f5" stroke-width="2"><circle cx="17" cy="17" r="15"/><path d="M11 10 l3 -1 l2 5 l-2 1.5 a9 9 0 0 0 4.5 4.5 l1.5 -2 l5 2 l-1 3 c-7 1 -14 -6 -13 -13z"/></svg>
    <div><div class="contact-label">CALL US</div><div class="contact-phone">555-014-7720</div></div>
  </div>
  <nav class="abs nav">
    <a class="active" href="#" style="margin-right:40px">HOME</a>
    <a href="#" style="margin-right:43px">ABOUT US</a>
    <a href="#" style="margin-right:43px">WOOD</a>
    <a href="#" style="margin-right:47px">PACKAGING</a>
    <a href="#">CONTACT US</a>
  </nav>
</header>

<section class="abs hero">
  <div class="abs hero-ship" role="img" aria-label="Aerial photo of a container ship sailing across blue ocean"></div>
  <h1 class="abs hero-title">PACKAGING A<br>GLOBAL TRADING<br>PARTNER YOU<br>CAN TRUST</h1>
  <a class="abs btn hero-btn" href="#">CONTACT US</a>
</section>

<section>
  <h2 class="abs intro-title">A <span>GLOBAL TRADING PARTNER</span> YOU CAN TRUST</h2>
  <div class="abs rule intro-rule"></div>
  <p class="abs intro-text">Lorem ipsum dolor sit amet, consectetur adipiscing elit, sed do eiusmod tempor incididunt ut labore et dolore magna aliqua. Ut enim ad minim veniam, quis nostrud exercitation ullamco laboris nisi ut aliquip ex ea commodo consequat. Duis aute irure dolor in reprehenderit in voluptate velit esse.</p>

  <div class="abs soft-band" role="img" aria-label="Decorative pale blue band beneath the cards"></div>
  <article class="abs card card-pack" role="img" aria-label="Photo of green crop rows in a farm field under blue sky">
    <div class="card-body">
      <h3 class="card-title">PACKAGING</h3>
      <p class="card-text">Lorem ipsum dolor sit amet consectetur adipiscing</p>
      <a class="btn card-btn" href="#">READ MORE</a>
    </div>
  </article>
  <article class="abs card card-wood" role="img" aria-label="Photo of white MDF cabinetry with an open drawer">
    <div class="card-body">
      <h3 class="card-title">MDF/WOOD</h3>
      <p class="card-text">Lorem ipsum dolor sit amet consectetur adipiscing</p>
      <a class="btn card-btn" href="#">READ MORE</a>
    </div>
  </article>
  <div class="abs card-badge"><i></i></div>
</section>

<section class="abs welcome">
  <div class="abs welcome-photo" role="img" aria-label="Photo of vacuum-sealed bags of carrots, broccoli and green beans"></div>
  <div class="abs welcome-kicker">WELCOME TO</div>
  <h2 class="abs welcome-title"><span>VELLORA</span><br>SOLUTIONS</h2>
  <div class="abs rule welcome-rule"></div>
  <p class="abs welcome-text">Lorem ipsum dolor sit amet, consectetur adipiscing elit, sed do eiusmod tempor incididunt ut labore et dolore magna aliqua. Ut enim ad minim veniam, quis nostrud exercitation ullamco laboris nisi ut aliquip ex ea commodo consequat. Duis aute irure dolor in reprehenderit in voluptate velit esse. eu fugiat nulla pariatur. Excepteur sint occaecat cupidatat non proident, sunt in culpa qui officia deserunt mollit anim id est laborum</p>
  <a class="abs btn welcome-btn" href="#">READ MORE</a>
</section>

<section>
  <article class="abs feature feat-forest" role="img" aria-label="Photo of a tall green forest">
    <div class="feat-box"><h3 class="feat-title">EXPERIENCE</h3><p class="feat-text">Lorem ipsum dolor sit amet, consectetur adipiscing elit, sed do eiusmod tempor incididunt ut labore et dolore magna aliqua</p><a class="btn feat-btn" href="#">READ MORE</a></div>
  </article>
  <article class="abs feature feat-port" role="img" aria-label="Photo of a container port with cranes at sunset">
    <div class="feat-box"><h3 class="feat-title">RISK MANAGEMENT</h3><p class="feat-text">Lorem ipsum dolor sit amet, consectetur adipiscing elit, sed do eiusmod tempor incididunt ut labore et dolore magna aliqua</p><a class="btn feat-btn" href="#">READ MORE</a></div>
  </article>
  <article class="abs feature feat-city" role="img" aria-label="Photo looking up at glass skyscrapers in sunlight">
    <div class="feat-box"><h3 class="feat-title">FINANCIAL STRENGTH</h3><p class="feat-text">Lorem ipsum dolor sit amet, consectetur adipiscing elit, sed do eiusmod tempor incididunt ut labore et dolore magna aliqua</p><a class="btn feat-btn" href="#">READ MORE</a></div>
  </article>
</section>

<footer class="abs footer">
  <div class="abs footer-mark">Vellora<br>Solutions</div>
  <div class="abs col-contact">
    <h4 class="col-title">CONTACT US</h4>
    <div class="info-row"><svg width="16" height="18" viewBox="0 0 16 18" fill="#0ea5f5"><path d="M8 0a6 6 0 0 0-6 6c0 5 6 12 6 12s6-7 6-12a6 6 0 0 0-6-6zm0 8.5a2.5 2.5 0 1 1 0-5 2.5 2.5 0 0 1 0 5z"/></svg><span>4417 KD Veldmere<br>Netherlands</span></div>
    <div class="info-row"><svg width="16" height="16" viewBox="0 0 16 16" fill="#0ea5f5"><path d="M3 1l3 0 1.5 4-2 1.5a8 8 0 0 0 4 4L11 8.5l4 1.5v3c-7 2-14-5-12-12z"/></svg><span>555-014-7720</span></div>
    <div class="info-row"><svg width="16" height="14" viewBox="0 0 16 14" fill="#0ea5f5"><path d="M0 1h16v12H0z M0 1l8 6 8-6" stroke="#e4f3fd" stroke-width="1.2"/></svg><span>Ivo.Lund@Vel-Lora.example</span></div>
  </div>
  <div class="abs col-menu">
    <h4 class="col-title">MENU</h4>
    <ul class="menu-list"><li>Home</li><li>Our Science</li><li>Collection</li><li>Results</li><li>About</li><li>Journal</li><li>Contact</li></ul>
  </div>
  <div class="abs col-follow">
    <h4 class="col-title">FOLLOW US</h4>
    <div class="social"><i></i><i></i><i></i><i></i><i></i></div>
  </div>
  <div class="abs footer-brand"><i></i><span>Vellora Solutions</span></div>
  <div class="abs footer-rule"></div>
  <p class="abs copyright">Copyright © 2026 All Rights Reserved</p>
</footer>

</body>
</html>
```